Power Generation Company needs a stationary design

We need a design for our letter envelope, A4 Envelope and letterhead. Our company name is BRIMVolt which i attached here sample our our call card. We are based in the Philippines and is into the Power Generation business. We own power facilities like Hydropower plant, Solar Power Plant, Diesel Power Plant, Gas Turbine Power Plant. We sell our power to various electric distribution companies, factories and office buildings.

Target Market(s)

Electric Distribution Companies and Factories

Industry/Entity Type

It Company

Colors
ec1f27

Requirements
Must have
• Logo and company name
Nice to have
• No specific
Should not have
• No specific

```html
<!DOCTYPE html>
<html lang="en">
<head>
<meta charset="utf-8">
<title>BRIMVolt Stationery</title>
<link href="https://fonts.googleapis.com/css2?family=Open+Sans:wght@400;600;700&display=swap" rel="stylesheet">
<style>
:root{
  --brand-red:#ec1f27;
  --deep-red:#a8121b;
  --envelope-red:#d63640;
  --ink:#555;
  --grey:#9a9a9a;
  --light-grey:#dcdcdc;
  --paper:#ffffff;
  --backdrop:#e9b7b8;
}
*{box-sizing:border-box;margin:0;padding:0}
html,body{width:1200px;height:850px;overflow:hidden}
body{background:var(--backdrop);font-family:"Open Sans",Arial,sans-serif;color:var(--ink);position:relative}
.sheet{position:absolute;background:var(--paper);box-shadow:0 6px 18px rgba(90,30,35,.25);overflow:hidden}

/* Letterhead A */
.letterhead-a{left:40px;top:150px;width:380px;height:537px}
.letterhead-a .top-band{position:absolute;left:0;top:0;width:100%;height:70px;background:linear-gradient(180deg,var(--deep-red),var(--brand-red) 60%,#c4161e)}
.letterhead-a .logo-tab{position:absolute;left:105px;top:16px;width:170px;height:62px;background:var(--paper);border-radius:10px 10px 0 0;text-align:center;padding-top:8px}
.brand-name{font-family:"Open Sans",Arial,sans-serif;font-weight:700;color:var(--brand-red);letter-spacing:1px;display:inline-flex;align-items:center;gap:6px}
.brand-name .dot{width:10px;height:10px;border-radius:50%;background:var(--brand-red);display:inline-block}
.letterhead-a .brand-name{font-size:24px}
.tagline{font-size:10px;font-weight:700;color:var(--grey);letter-spacing:1px}
.faint-name{position:absolute;font-weight:700;color:#ececec;letter-spacing:6px}
.letterhead-a .faint-name{left:30px;top:370px;font-size:54px}
.bottom-band{position:absolute;left:0;bottom:0;width:100%;height:10px;background:linear-gradient(90deg,#f04a7a,var(--brand-red) 40%,var(--deep-red))}

/* Contact block */
.contact{position:absolute;font-size:6px;line-height:1.6;color:var(--ink)}
.contact .label{display:inline-block;background:var(--light-grey);color:var(--brand-red);font-weight:700;padding:1px 14px;border-left:2px solid var(--brand-red);border-right:2px solid var(--brand-red);margin-left:120px;margin-bottom:3px}
.contact .rule{height:1px;background:var(--light-grey);margin-bottom:3px}
.contact .row{display:flex;gap:10px;align-items:center;white-space:nowrap}
.icon{width:8px;height:8px;vertical-align:middle;margin-right:3px}
.letterhead-a .contact{left:20px;right:20px;bottom:16px}

/* Envelope back */
.envelope-back{left:450px;top:195px;width:330px;height:165px;background:var(--envelope-red)}
.envelope-back svg{position:absolute;left:0;top:0}

/* Envelope front */
.envelope-front{left:450px;top:390px;width:330px;height:165px}
.envelope-front .top-band{position:absolute;left:0;top:0;width:100%;height:22px;background:linear-gradient(180deg,var(--deep-red),var(--brand-red))}
.envelope-front .logo{position:absolute;left:18px;top:34px}
.envelope-front .brand-name{font-size:17px}
.envelope-front .tagline{font-size:8px}
.envelope-front .contact{left:14px;right:14px;bottom:10px;font-size:5.2px;line-height:1.5}
.envelope-front .contact .label{margin-left:100px}
.envelope-front .icon{width:7px;height:7px}
.envelope-front .bottom-band{height:6px;background:linear-gradient(90deg,var(--brand-red),var(--deep-red))}

/* Letterhead B */
.letterhead-b{left:810px;top:150px;width:380px;height:537px}
.letterhead-b .rule-red{position:absolute;left:0;top:52px;width:110px;height:4px;background:var(--brand-red)}
.letterhead-b .rule-grey{position:absolute;right:0;top:14px;width:90px;height:4px;background:#b5b5b5}
.letterhead-b .logo{position:absolute;left:118px;top:22px}
.letterhead-b .brand-name{font-size:22px}
.services{position:absolute;left:118px;top:52px;font-size:5.5px;font-weight:700;color:#333;white-space:nowrap}
.services span::before{content:"▸ ";color:var(--brand-red)}
.letterhead-b .contact{left:20px;right:20px;bottom:18px}
.letterhead-b .foot-lines{position:absolute;left:0;bottom:6px;width:100%;height:6px}
.letterhead-b .foot-lines .grey{position:absolute;left:0;top:0;width:45%;height:3px;background:#c9c9c9}
.letterhead-b .foot-lines .red{position:absolute;right:0;top:0;width:55%;height:4px;background:var(--brand-red)}
</style>
</head>
<body>

<svg width="0" height="0" style="position:absolute">
  <defs>
    <symbol id="icon-pin" viewBox="0 0 10 10"><circle cx="5" cy="5" r="5" fill="#ec1f27"/><path d="M5 2.2a1.8 1.8 0 0 1 1.8 1.8C6.8 5.4 5 7.8 5 7.8S3.2 5.4 3.2 4A1.8 1.8 0 0 1 5 2.2z" fill="#fff"/></symbol>
    <symbol id="icon-phone" viewBox="0 0 10 10"><circle cx="5" cy="5" r="5" fill="#ec1f27"/><rect x="3.5" y="2.3" width="3" height="5.4" rx=".6" fill="#fff"/></symbol>
    <symbol id="icon-mail" viewBox="0 0 10 10"><circle cx="5" cy="5" r="5" fill="#ec1f27"/><rect x="2.6" y="3.3" width="4.8" height="3.4" fill="#fff"/><path d="M2.6 3.3 5 5.2 7.4 3.3" stroke="#ec1f27" stroke-width=".5" fill="none"/></symbol>
    <symbol id="icon-web" viewBox="0 0 10 10"><circle cx="5" cy="5" r="5" fill="#ec1f27"/><circle cx="5" cy="5" r="2.4" fill="none" stroke="#fff" stroke-width=".7"/></symbol>
  </defs>
</svg>

<!-- Letterhead with band -->
<section class="sheet letterhead-a">
  <div class="top-band"></div>
  <div class="logo-tab">
    <div class="brand-name"><span class="dot"></span>BRIMVolt</div>
    <div class="tagline">BRIMVolt Inc.</div>
  </div>
  <div class="faint-name">BRIMVolt</div>
  <div class="contact">
    <div class="label">Contact Detail</div>
    <div class="rule"></div>
    <div class="row"><span><svg class="icon"><use href="#icon-pin"/></svg>88 Harbor View Tower, 402 Narra Ave., Lakeside Business Park, Bayside, Pasig City, 1600 Philippines</span></div>
    <div class="row">
      <span><svg class="icon"><use href="#icon-phone"/></svg>+632 555 0140</span>
      <span><svg class="icon"><use href="#icon-phone"/></svg>+632 555 0141</span>
      <span><svg class="icon"><use href="#icon-phone"/></svg>+63 917 555 0192</span>
    </div>
    <div class="row">
      <span><svg class="icon"><use href="#icon-mail"/></svg>mreyes@brimvolt-energy.com</span>
      <span><svg class="icon"><use href="#icon-web"/></svg>www.brimvolt-energy.com</span>
    </div>
  </div>
  <div class="bottom-band"></div>
</section>

<!-- Envelope back -->
<section class="sheet envelope-back" aria-label="Envelope back">
  <svg width="330" height="165" viewBox="0 0 330 165">
    <path d="M0 0 L165 110 L330 0" fill="none" stroke="#b32630" stroke-width="1.5"/>
  </svg>
</section>

<!-- Envelope front -->
<section class="sheet envelope-front">
  <div class="top-band"></div>
  <div class="logo">
    <div class="brand-name"><span class="dot"></span>BRIMVolt</div>
    <div class="tagline">BRIMVolt Inc.</div>
  </div>
  <div class="contact">
    <div class="label">Contact Detail</div>
    <div class="rule"></div>
    <div class="row"><span><svg class="icon"><use href="#icon-pin"/></svg>88 Harbor View Tower, 402 Narra Ave., Lakeside Business Park, Bayside, Pasig City, 1600 Philippines</span></div>
    <div class="row">
      <span><svg class="icon"><use href="#icon-phone"/></svg>+632 555 0140</span>
      <span><svg class="icon"><use href="#icon-phone"/></svg>+632 555 0141</span>
      <span><svg class="icon"><use href="#icon-phone"/></svg>+63 917 555 0192</span>
    </div>
    <div class="row">
      <span><svg class="icon"><use href="#icon-mail"/></svg>mreyes@brimvolt-energy.com</span>
      <span><svg class="icon"><use href="#icon-web"/></svg>www.brimvolt-energy.com</span>
    </div>
  </div>
  <div class="bottom-band"></div>
</section>

<!-- Letterhead with services -->
<section class="sheet letterhead-b">
  <div class="rule-grey"></div>
  <div class="rule-red"></div>
  <div class="logo"><div class="brand-name"><span class="dot"></span>BRIMVolt</div></div>
  <div class="services"><span>Hydropower plant</span> <span>Solar Power Plant</span> <span>Diesel Power Plant</span> <span>Gas Turbine Power Plant</span></div>
  <div class="contact">
    <div class="label">Contact Detail</div>
    <div class="rule"></div>
    <div class="row"><span><svg class="icon"><use href="#icon-pin"/></svg>88 Harbor View Tower, 402 Narra Ave., Lakeside Business Park, Bayside, Pasig City, 1600 Philippines</span></div>
    <div class="row">
      <span><svg class="icon"><use href="#icon-phone"/></svg>+632 555 0140</span>
      <span><svg class="icon"><use href="#icon-phone"/></svg>+632 555 0141</span>
      <span><svg class="icon"><use href="#icon-phone"/></svg>+63 917 555 0192</span>
    </div>
    <div class="row">
      <span><svg class="icon"><use href="#icon-mail"/></svg>mreyes@brimvolt-energy.com</span>
      <span><svg class="icon"><use href="#icon-web"/></svg>www.brimvolt-energy.com</span>
    </div>
  </div>
  <div class="foot-lines"><div class="grey"></div><div class="red"></div></div>
</section>

</body>
</html>
```